Warranty Card Design for Mattress Brand

We would like to design a warranty card for our mattresses,
it consists of 2 pages in one card (front and back) to be neatly showing our warranty details/text , our logo , our website, address and telephone clearly.

Target Market(s)

household

Font styles to use
Serif
Script

Colors
3277b5
33a6d7
85cae6
0492cd
3176b5
0355a3
85abd2
cee9f5
85acd3

Requirements
Must have
• a nice warranty logo
Nice to have
• a nice warranty logo with a neat text and clear layout, colors have to be related to the logo

```html
<!DOCTYPE html>
<html lang="en">
<head>
<meta charset="utf-8">
<title>slumbra – Warranty Card</title>
<link rel="stylesheet" href="https://fonts.googleapis.com/css2?family=Open+Sans:wght@300;400;600;700&display=swap">
<style>
  :root {
    --brand-blue: #5378bb;
    --paper: #ffffff;
    --ink: #3d3d3d;
    --backdrop: #eeeff1;
  }
  * { box-sizing: border-box; margin: 0; padding: 0; }
  html, body { width: 1200px; height: 1200px; overflow: hidden; }
  body {
    background: var(--backdrop);
    font-family: "Open Sans", Arial, sans-serif;
    position: relative;
  }
  .card {
    position: absolute;
    top: 181px;
    width: 382px;
    height: 845px;
    overflow: hidden;
  }
  .card--front { left: 207px; background: var(--paper); }
  .card--back { left: 610px; width: 386px; background: var(--brand-blue); color: var(--paper); }

  .brand {
    position: absolute;
    left: 0; right: 0;
    text-align: center;
  }
  .brand__name {
    display: block;
    font-weight: 300;
    font-size: 76px;
    line-height: 1;
    letter-spacing: 1px;
  }
  .brand__tagline {
    display: block;
    font-weight: 400;
    font-size: 13px;
    letter-spacing: 4px;
    margin-top: 14px;
  }
  .card--front .brand { top: 82px; color: var(--brand-blue); }
  .card--back .brand { top: 62px; }
  .card--back .brand__name { font-size: 66px; }
  .card--back .brand__tagline { font-size: 11.5px; margin-top: 10px; }

  .front-decor {
    position: absolute;
    right: -170px;
    bottom: -170px;
    width: 400px;
    height: 400px;
    border-radius: 50%;
    background: var(--brand-blue);
  }

  .address {
    position: absolute;
    left: 32px;
    top: 360px;
    font-size: 19.5px;
    line-height: 24px;
    color: var(--ink);
  }
  .contacts {
    position: absolute;
    left: 32px;
    top: 444px;
    list-style: none;
    font-size: 18.5px;
    color: var(--ink);
  }
  .contacts li {
    display: flex;
    align-items: center;
    height: 26px;
    margin-bottom: 1px;
  }
  .contacts svg { width: 17px; height: 17px; margin-right: 10px; flex: none; }

  .fields {
    position: absolute;
    left: 29px;
    right: 26px;
    top: 278px;
    list-style: none;
  }
  .fields li {
    display: flex;
    align-items: flex-end;
    height: 36px;
    font-size: 18px;
    font-weight: 600;
  }
  .fields .fill {
    flex: 1;
    border-bottom: 3px dotted var(--paper);
    margin-bottom: 6px;
    margin-left: 1px;
  }

  .exclusions {
    position: absolute;
    left: 29px;
    right: 40px;
    top: 505px;
  }
  .exclusions h2 {
    display: inline-block;
    font-size: 13.5px;
    font-weight: 700;
    padding-bottom: 2px;
    border-bottom: 1.5px solid var(--paper);
    margin-bottom: 14px;
  }
  .exclusions ul { list-style: none; }
  .exclusions li {
    position: relative;
    padding-left: 14px;
    font-size: 12px;
    line-height: 13.5px;
    margin-bottom: 6.5px;
  }
  .exclusions li::before {
    content: "";
    position: absolute;
    left: 0; top: 5px;
    width: 5px; height: 5px;
    border-radius: 50%;
    background: var(--paper);
  }
</style>
</head>
<body>
  <section class="card card--front">
    <div class="brand">
      <span class="brand__name">slumbra</span>
      <span class="brand__tagline">mattresses &amp; Pillows</span>
    </div>

    <div class="front-decor"></div>

    <p class="address">Hadi Salem and Sons<br>Cedar Hill, Factory Road,<br>Baabda, Lebanon</p>

    <ul class="contacts">
      <li>
        <svg viewBox="0 0 24 24" fill="#5378bb"><path d="M6.6 10.8a15.1 15.1 0 0 0 6.6 6.6l2.2-2.2c.3-.3.7-.4 1-.2 1.1.4 2.3.6 3.6.6.6 0 1 .4 1 1V20c0 .6-.4 1-1 1A17 17 0 0 1 3 4c0-.6.4-1 1-1h3.5c.6 0 1 .4 1 1 0 1.3.2 2.5.6 3.6.1.3 0 .7-.2 1z"/></svg>
        +961 1 555 010
      </li>
      <li>
        <svg viewBox="0 0 24 24" fill="#5378bb"><path d="M2 5h20v14H2z"/><path d="M2 5l10 8 10-8M2 19l7-7M22 19l-7-7" fill="none" stroke="#fff" stroke-width="1.6"/></svg>
        info@slumbrahome.com
      </li>
      <li>
        <svg viewBox="0 0 24 24" fill="none" stroke="#5378bb" stroke-width="1.5"><circle cx="12" cy="12" r="9.5"/><ellipse cx="12" cy="12" rx="4.5" ry="9.5"/><path d="M2.5 12h19M4 7h16M4 17h16"/></svg>
        www.hadisalemandsons.com
      </li>
    </ul>
  </section>

  <section class="card card--back">
    <div class="brand">
      <span class="brand__name">slumbra</span>
      <span class="brand__tagline">mattresses &amp; Pillows</span>
    </div>

    <ul class="fields">
      <li>Invoice Number:<span class="fill"></span></li>
      <li>Warranty Period:<span class="fill"></span></li>
      <li><span class="fill"></span></li>
      <li>Date:<span class="fill"></span></li>
    </ul>

    <div class="exclusions">
      <h2>Mattress Warranty does not cover the following:</h2>
      <ul>
        <li>Comfort preference</li>
        <li>Fabric Stains, soiling or burns</li>
        <li>Body impressions of less than 3cm</li>
        <li>Damage to the mattress due to abuse</li>
        <li>Bent Perimeter border rods due to moving<br>or bending the mattress</li>
        <li>Size allowance of +/- 2cm</li>
        <li>Bed Bugs and Dust Mites</li>
        <li>Mattress Odor: as in any upholstery, new mattress may have odor that will fade with time.</li>
        <li>For Latex and Memory Foam mattresses:<br>normal change in softness and recovery time in these materials with time. This does not affect the relieving qualities of these mattresses.</li>
        <li>Transportation and Inspection Costs</li>
      </ul>
    </div>
  </section>
</body>
</html>
```